Xmas banner Lathermoss handmade skincare

We need a xmas sale banner for our skincare website and a few different ones for instagram. Our website is www.lathermoss.example, you can use any of our products to include in the banner. We also have some nice product group pictures on our instagram.com/lathermoss. If you could include a christmassy message for example "its beginning to feel alot like christmas".

Target Market(s)

Women, 18-35, luxury, handmade natural shoppers

Requirements
Must have
• See our site and instagram. You have creative freedom.
Nice to have
• Try incorporating our products in imaginative ways, for example using bath bombs as Christmas tree baubles
Should not have
• Dont send anything if you think it will look out of place.

```html
<!DOCTYPE html>
<html lang="en">
<head>
<meta charset="utf-8">
<title>Lathermoss Christmas Banner Set</title>
<link rel="stylesheet" href="https://fonts.googleapis.com/css2?family=Arimo:ital,wght@0,400;0,700;1,400&display=swap">
<style>
  :root {
    --orange: #f26a1b;
    --orange-deep: #e2531a;
    --orange-glow: #fb9a4e;
    --peach: #f9c7a6;
    --sky: #8fd4f5;
    --periwinkle: #9ba4dc;
    --navy: #1f2c6e;
    --white: #ffffff;
    --ink: #111111;
    --skin-light: #f1d4c2;
    --skin-mid: #d9ab92;
    --jar-cream: #f3efe2;
    --jar-lid: #d9dadb;
  }
  * { box-sizing: border-box; margin: 0; padding: 0; }
  html, body { width: 1200px; height: 1200px; overflow: hidden; background: var(--white); }
  body { position: relative; font-family: "Arimo", Arial, sans-serif; }

  .banner { position: absolute; overflow: hidden; border: 1px solid #555; background: var(--white); }
  .banner-bg { position: absolute; inset: 0; width: 100%; height: 100%; }
  .size-label { position: absolute; font-size: 20px; color: var(--ink); letter-spacing: 0.5px; }

  .photo-model {
    position: absolute;
    background: radial-gradient(ellipse at 50% 40%, var(--skin-light) 0%, var(--skin-mid) 55%, rgba(217,171,146,0) 80%);
  }
  .photo-jar {
    position: absolute;
    border-radius: 18% / 14%;
    background: linear-gradient(180deg, var(--jar-lid) 0%, #eeeeee 30%, var(--jar-cream) 34%, #e8e2cf 100%);
    box-shadow: 0 4px 10px rgba(0,0,0,0.15);
  }

  .headline { position: absolute; color: var(--white); line-height: 1.05; }
  .organic { position: absolute; color: var(--white); }

  .cta {
    position: absolute;
    display: flex; align-items: center; justify-content: center; gap: 0.5em;
    background: linear-gradient(180deg, #ff8a3a 0%, var(--orange) 45%, var(--orange-deep) 100%);
    color: var(--white); font-weight: 700;
    border-radius: 6px;
    box-shadow: 0 4px 6px rgba(0,0,0,0.3);
  }
  .cta svg { flex: none; }

  /* 728x90 leaderboard */
  .banner-leaderboard { left: 103px; top: 31px; width: 1027px; height: 126px; }
  .banner-leaderboard .headline { left: 176px; top: 10px; font-size: 22px; }
  .banner-leaderboard .organic { left: 790px; top: 12px; font-size: 31px; }
  .banner-leaderboard .cta { left: 809px; top: 56px; width: 183px; height: 50px; font-size: 20px; }

  /* 300x250 rectangle */
  .banner-rectangle { left: 103px; top: 216px; width: 425px; height: 352px; }
  .banner-rectangle .headline { left: 19px; top: 10px; font-size: 22px; color: var(--navy); line-height: 1.1; }
  .banner-rectangle .organic { left: 19px; top: 144px; font-size: 23px; font-style: italic; color: var(--orange); }
  .banner-rectangle .cta { left: 99px; top: 281px; width: 184px; height: 50px; font-size: 20px; }

  /* 1080x1080 square */
  .banner-square { left: 103px; top: 600px; width: 563px; height: 563px; }
  .banner-square .headline { left: 17px; top: 10px; font-size: 35px; font-weight: 700; line-height: 1.15; }
  .banner-square .organic { left: 94px; top: 488px; font-size: 30px; }
  .banner-square .cta { left: 315px; top: 479px; width: 225px; height: 61px; font-size: 26px; }

  /* 160x600 skyscraper */
  .banner-skyscraper { left: 854px; top: 230px; width: 225px; height: 846px; }
  .banner-skyscraper .headline { left: 0; right: 0; top: 16px; text-align: center; font-size: 27px; }
  .banner-skyscraper .organic { left: 0; right: 0; top: 730px; text-align: center; font-size: 24px; }
  .banner-skyscraper .cta { left: 21px; top: 771px; width: 184px; height: 50px; font-size: 20px; }
</style>
</head>
<body>

<!-- Leaderboard -->
<section class="banner banner-leaderboard">
  <svg class="banner-bg" viewBox="0 0 1027 126" preserveAspectRatio="none" aria-hidden="true">
    <defs>
      <radialGradient id="lb-orange" cx="0.15" cy="0.5" r="0.8">
        <stop offset="0" stop-color="#fb9a4e"/><stop offset="1" stop-color="#ee5f18"/>
      </radialGradient>
    </defs>
    <polygon points="0,0 590,0 470,126 0,126" fill="var(--peach)"/>
    <polygon points="0,0 571,0 452,126 0,126" fill="url(#lb-orange)"/>
    <polygon points="571,0 625,0 750,126 700,126" fill="var(--sky)"/>
    <polygon points="610,0 1027,0 1027,126 750,126" fill="var(--periwinkle)"/>
  </svg>
  <div class="photo-model" role="img" aria-label="Photo of a woman with her hands framing her face" style="left:8px;top:0;width:150px;height:126px;"></div>
  <h2 class="headline">IT’S BEGINNING TO FEEL<br>ALOT LIKE CHRISTMAS</h2>
  <div class="photo-jar" role="img" aria-label="Photo of a Lathermoss body butter jar" style="left:488px;top:10px;width:128px;height:116px;"></div>
  <p class="organic">100% Organic</p>
  <a class="cta">BUY NOW!
    <svg width="30" height="30" viewBox="0 0 30 30" aria-hidden="true"><circle cx="15" cy="15" r="14" fill="var(--white)"/><path d="M8 12.5h8v-4.5l7 7-7 7v-4.5h-8z" fill="var(--orange)"/></svg>
  </a>
</section>
<span class="size-label" style="left:574px;top:174px;">728X90</span>

<!-- Medium rectangle -->
<section class="banner banner-rectangle">
  <svg class="banner-bg" viewBox="0 0 425 352" preserveAspectRatio="none" aria-hidden="true">
    <defs>
      <radialGradient id="rect-orange" cx="0.65" cy="0.35" r="0.6">
        <stop offset="0" stop-color="#fb9a4e"/><stop offset="1" stop-color="#ee5f18"/>
      </radialGradient>
    </defs>
    <polygon points="175,0 425,0 425,150 285,215" fill="var(--peach)"/>
    <polygon points="200,0 425,0 425,140 310,205" fill="url(#rect-orange)"/>
    <polygon points="0,300 425,120 425,352 0,352" fill="var(--sky)"/>
    <polygon points="0,320 425,150 425,352 0,352" fill="var(--periwinkle)"/>
  </svg>
  <div class="photo-model" role="img" aria-label="Photo of a woman with her hands framing her face" style="left:185px;top:0;width:240px;height:320px;"></div>
  <h2 class="headline">IT’S<br>BEGINNING<br>TO FEEL<br>]ALOT LIKE<br>CHRISTMAS</h2>
  <p class="organic">100% Organic</p>
  <div class="photo-jar" role="img" aria-label="Photo of a Lathermoss body butter jar" style="left:21px;top:176px;width:137px;height:128px;"></div>
  <a class="cta">BUY NOW!
    <svg width="30" height="30" viewBox="0 0 30 30" aria-hidden="true"><circle cx="15" cy="15" r="14" fill="var(--white)"/><path d="M8 12.5h8v-4.5l7 7-7 7v-4.5h-8z" fill="var(--orange)"/></svg>
  </a>
</section>
<span class="size-label" style="left:548px;top:345px;">300X250</span>

<!-- Square -->
<section class="banner banner-square">
  <svg class="banner-bg" viewBox="0 0 563 563" preserveAspectRatio="none" aria-hidden="true">
    <defs>
      <radialGradient id="sq-orange" cx="0.3" cy="0.35" r="0.6">
        <stop offset="0" stop-color="#fb9a4e"/><stop offset="1" stop-color="#ee5f18"/>
      </radialGradient>
    </defs>
    <rect width="563" height="563" fill="url(#sq-orange)"/>
    <path d="M0,180 C150,150 300,110 563,60 L563,563 L0,563 Z" fill="var(--peach)"/>
    <path d="M60,200 C200,150 380,110 563,85 L563,563 L0,563 L0,260 Z" fill="var(--white)"/>
    <polygon points="0,470 563,370 563,563 0,563" fill="var(--sky)"/>
    <polygon points="0,490 563,392 563,563 0,563" fill="var(--periwinkle)"/>
  </svg>
  <div class="photo-model" role="img" aria-label="Photo of a woman with her hands framing her face" style="left:34px;top:70px;width:300px;height:493px;"></div>
  <h2 class="headline">It’s Beginning to Feel<br>Alot Like Christmas</h2>
  <div class="photo-jar" role="img" aria-label="Photo of a Lathermoss body butter jar" style="left:327px;top:144px;width:222px;height:275px;"></div>
  <p class="organic">100% Organic</p>
  <a class="cta">BUY NOW!
    <svg width="38" height="38" viewBox="0 0 30 30" aria-hidden="true"><circle cx="15" cy="15" r="14" fill="var(--white)"/><path d="M8 12.5h8v-4.5l7 7-7 7v-4.5h-8z" fill="var(--orange)"/></svg>
  </a>
</section>
<span class="size-label" style="left:676px;top:880px;">1080X1080</span>

<!-- Skyscraper -->
<section class="banner banner-skyscraper">
  <svg class="banner-bg" viewBox="0 0 225 846" preserveAspectRatio="none" aria-hidden="true">
    <defs>
      <linearGradient id="sk-orange" x1="0" y1="0" x2="0" y2="1">
        <stop offset="0" stop-color="#ee5f18"/><stop offset="0.5" stop-color="#fb9a4e"/><stop offset="1" stop-color="#f47a2c"/>
      </linearGradient>
    </defs>
    <rect width="225" height="846" fill="url(#sk-orange)"/>
    <polygon points="0,520 225,330 225,846 0,846" fill="var(--peach)"/>
    <polygon points="30,560 225,350 225,846 0,846 0,600" fill="var(--white)"/>
    <polygon points="0,640 225,380 225,846 0,846" fill="var(--sky)"/>
    <polygon points="0,665 225,405 225,846 0,846" fill="var(--periwinkle)"/>
  </svg>
  <div class="photo-model" role="img" aria-label="Photo of a woman with her hand beneath her chin" style="left:0;top:145px;width:225px;height:470px;"></div>
  <h2 class="headline">IMPROVE THE<br>OVERALL<br>HEALTH OF<br>YOUR SKIN</h2>
  <div class="photo-jar" role="img" aria-label="Photo of a Lathermoss body butter jar" style="left:35px;top:571px;width:172px;height:148px;"></div>
  <p class="organic">100% Organic</p>
  <a class="cta">BUY NOW!
    <svg width="30" height="30" viewBox="0 0 30 30" aria-hidden="true"><circle cx="15" cy="15" r="14" fill="var(--white)"/><path d="M8 12.5h8v-4.5l7 7-7 7v-4.5h-8z" fill="var(--orange)"/></svg>
  </a>
</section>
<span class="size-label" style="left:906px;top:1098px;">160X600</span>

</body>
</html>
```